Online counselling service - business cards

We need a business card (front and back) design for a new online counselling and psychotherapy service for people all over the world. We offer voice- and video-chat for clients, as well as instant messaging.
The final design should communicate a fusion of calm, strength and support.

Industry/Entity Type

Business

Requirements
Must have
• The design must contain the following information:
Company name - Quiet Harbour Path
E-mail address - admin@quietharbourpath-example.com
Website address - www.quietharbourpath-example.com

The design must also include the logo (with or without words), as attached below.
Nice to have
• We are open to QR codes being used.
A minimalist approach to design is preferred for the front of the card, with the eye drawn to the name of the company.
Sans-serif fonts only, please.
It would be great to have a space for therapists to put their name (but no other contact details) on the back of the card.
After seeing different designs, I like the feel of rounded corner business cards.
If you want to have a bash at redesigning the logo you are very welcome to do so!
Should not have
• The design should avoid using sharp angles and serif-fonts.

```html
<!DOCTYPE html>
<html lang="en">
<head>
<meta charset="utf-8">
<title>Quiet Harbour Path – Business Cards</title>
<link rel="stylesheet" href="https://fonts.googleapis.com/css2?family=Arimo:wght@400;700&display=swap">
<style>
  :root {
    --backdrop: #e8e5e1;
    --card-grey: #dedfe1;
    --card-light: #eef0f2;
    --blue-deep: #0d5bb5;
    --blue-mid: #1f76d2;
    --blue-bright: #3a93e8;
    --blue-band: #0b4e9e;
    --ink-blue: #1565c0;
    --ink-grey: #5c6670;
    --white: #ffffff;
  }
  * { box-sizing: border-box; margin: 0; padding: 0; }
  html, body { width: 1200px; height: 800px; overflow: hidden; }
  body {
    background: var(--backdrop);
    font-family: "Arimo", Arial, sans-serif;
    position: relative;
  }
  .card {
    position: absolute;
    width: 452px;
    height: 276px;
    border-radius: 4px;
    overflow: hidden;
    box-shadow: 0 6px 16px rgba(0,0,0,0.18);
  }
  .card--front { left: 238px; top: 96px; background: linear-gradient(180deg, var(--card-light), var(--card-grey)); }
  .card--back { left: 485px; top: 400px; background: var(--card-grey); }

  /* front */
  .front-panel { position: absolute; inset: 0; }
  .front-brand {
    position: absolute; left: 20px; top: 96px; width: 240px;
    display: flex; align-items: center; justify-content: center; gap: 10px;
    color: var(--white); font-weight: 700; font-size: 19px;
  }
  .brand-dot { width: 14px; height: 14px; border-radius: 50%; background: var(--white); flex: none; }
  .front-tagline {
    position: absolute; left: 14px; top: 233px;
    color: var(--white); font-size: 10px; letter-spacing: 0.1px;
  }
  .front-tagline strong { font-weight: 700; }
  .services {
    position: absolute; right: 14px; top: 14px;
    display: flex; gap: 12px;
  }
  .service { width: 42px; text-align: center; }
  .service-icon {
    width: 36px; height: 36px; border-radius: 50%; margin: 0 auto;
    background: radial-gradient(circle at 40% 35%, #ffffff, #b9bfc6);
    box-shadow: 0 1px 3px rgba(0,0,0,0.25);
    display: flex; align-items: center; justify-content: center;
  }
  .service-label { margin-top: 6px; font-size: 5px; color: var(--ink-blue); white-space: nowrap; }
  .service-label strong { font-weight: 700; }
  .company-name {
    position: absolute; right: 16px; top: 182px;
    font-size: 14px; color: var(--ink-blue);
  }
  .company-name strong { font-weight: 700; }
  .contact-list {
    position: absolute; right: 16px; top: 204px;
    border-top: 1px solid #b7bec6; padding-top: 5px;
    list-style: none;
  }
  .contact-item {
    display: flex; align-items: center; gap: 5px;
    font-size: 9.5px; color: var(--ink-grey); line-height: 16px;
  }
  .contact-icon {
    width: 12px; height: 10px; background: var(--ink-blue); border-radius: 2px;
    display: flex; align-items: center; justify-content: center;
  }

  /* back */
  .back-face {
    position: absolute; left: 0; right: 0; top: 12px; bottom: 18px;
    background: radial-gradient(ellipse at 50% 45%, var(--blue-bright), var(--blue-mid) 45%, var(--blue-deep));
    display: flex; align-items: center; justify-content: center; gap: 10px;
  }
  .back-brand { color: var(--white); font-weight: 700; font-size: 18px; }
</style>
</head>
<body>

<section class="card card--front" aria-label="Front of business card">
  <svg class="front-panel" width="452" height="276" viewBox="0 0 452 276" aria-hidden="true">
    <defs>
      <linearGradient id="panelBlue" x1="0" y1="0" x2="1" y2="1">
        <stop offset="0" stop-color="#2a86e0"/>
        <stop offset="1" stop-color="#0c57ad"/>
      </linearGradient>
    </defs>
    <polygon points="0,12 252,12 296,138 252,262 0,262" fill="url(#panelBlue)"/>
    <rect x="0" y="226" width="252" height="22" fill="#0b4e9e" opacity="0.55"/>
  </svg>

  <div class="front-brand"><span class="brand-dot"></span>Quiet Harbour Path</div>
  <p class="front-tagline">counselling and <strong>PSYCHOTHERAPY SERVICE</strong></p>

  <div class="services">
    <div class="service">
      <div class="service-icon">
        <svg width="18" height="12" viewBox="0 0 18 12"><rect x="0" y="1" width="12" height="10" rx="2" fill="#1565c0"/><polygon points="12,6 18,2 18,10" fill="#1565c0"/></svg>
      </div>
      <p class="service-label">video <strong>CHAT</strong></p>
    </div>
    <div class="service">
      <div class="service-icon">
        <svg width="18" height="16" viewBox="0 0 18 16"><rect x="0" y="0" width="18" height="11" rx="3" fill="#1565c0"/><polygon points="4,10 9,10 4,15" fill="#1565c0"/></svg>
      </div>
      <p class="service-label">voice <strong>CHAT</strong></p>
    </div>
    <div class="service">
      <div class="service-icon">
        <svg width="12" height="18" viewBox="0 0 12 18"><rect x="0" y="0" width="12" height="18" rx="2" fill="#1565c0"/><rect x="2" y="2" width="8" height="11" fill="#ffffff"/><circle cx="6" cy="15.5" r="1.2" fill="#ffffff"/></svg>
      </div>
      <p class="service-label">instant <strong>MESSAGING</strong></p>
    </div>
  </div>

  <p class="company-name">Quiet Harbour <strong>PATH</strong></p>
  <ul class="contact-list">
    <li class="contact-item">
      <span class="contact-icon"><svg width="8" height="6" viewBox="0 0 8 6"><polyline points="0,0 4,3.5 8,0" fill="none" stroke="#fff" stroke-width="1"/></svg></span>
      admin@quietharbourpath-example.com
    </li>
    <li class="contact-item">
      <span class="contact-icon"><svg width="8" height="8" viewBox="0 0 8 8"><circle cx="4" cy="4" r="3.3" fill="none" stroke="#fff" stroke-width="0.9"/><line x1="0.7" y1="4" x2="7.3" y2="4" stroke="#fff" stroke-width="0.8"/></svg></span>
      www.quietharbourpath-example.com
    </li>
  </ul>
</section>

<section class="card card--back" aria-label="Back of business card">
  <div class="back-face">
    <span class="brand-dot"></span>
    <span class="back-brand">Quiet Harbour Path</span>
  </div>
</section>

</body>
</html>
```